Create banner ads for a digital product that deletes personal information from the web

The context of the banners is general advertisement for our service.
Please provide us with a set of static and flash/gif banners in the following standard sizes for the theme you create:
160x600
300x250
300x600
320x250
336x280
728x90
Please see our website for logo (just our name) and theme ideas - please follow similar color/font schemes if possible. www.quietlanternhub.com
Our company is an online service that deletes personal information from the internet for our members (automated opt-outs and content removal). Our target audience is anyone who wishes to protect their personal information from being on the internet (i.e. prefer to fly under the internet radar, for example). This is a product for U.S. residents who value privacy and online reputation. We seek to provide members with control of what 300+ websites are sharing about them – removing names, addresses, ages, phone numbers, email addresses, children’s information, home/property value information etc.
Industry/Entity Type
Internet
Look and feel
Each slider illustrates characteristics of the customer's brand and the style your logo design should communicate.

```html
<!DOCTYPE html>
<html lang="en">
<head>
<meta charset="utf-8">
<title>QuietLanternHub – Banner Set</title>
<link rel="stylesheet" href="https://fonts.googleapis.com/css2?family=Cutive&family=Baloo+2:wght@800&family=Michroma&family=Open+Sans:wght@600;700&family=Roboto:wght@700&display=swap">
<style>
  :root{
    --page:#f2f2f2;
    --brand-blue:#4f76ad;
    --brand-blue-dark:#23467e;
    --leaf-green:#5cb85c;
    --leaf-green-dark:#3f9a45;
    --sky-top:#bcd6f0;
    --sky-mid:#e4f0fb;
    --sky-light:#ffffff;
    --gold-top:#ffe45c;
    --gold-bottom:#f2a900;
    --caption:#b3b3b3;
    --white:#ffffff;
    --ink:#1b1b1b;
  }
  *{box-sizing:border-box;margin:0;padding:0}
  html,body{width:1200px;height:1046px;overflow:hidden}
  body{background:var(--page);position:relative;font-family:"Open Sans",sans-serif}

  .banner{position:absolute;overflow:hidden;border:1px solid #c9d3df;--k:1}
  .scene{position:absolute;inset:0;
    background:
      radial-gradient(ellipse 45% 60% at 50% 100%, var(--sky-light) 0%, rgba(255,255,255,0) 70%),
      linear-gradient(180deg,var(--sky-top) 0%,var(--sky-mid) 55%,#cfe2f5 100%);}

  .brand-name{font-family:"Cutive",serif;color:var(--white);white-space:nowrap}
  .headline{font-family:"Baloo 2",sans-serif;font-weight:800;color:var(--white);letter-spacing:-.5px;white-space:nowrap;
    text-shadow:-2px -2px 0 var(--brand-blue-dark),2px -2px 0 var(--brand-blue-dark),-2px 2px 0 var(--brand-blue-dark),2px 2px 0 var(--brand-blue-dark),0 3px 4px rgba(0,0,0,.25)}
  .service{background:var(--leaf-green);color:var(--white);font-weight:600;text-align:center}
  .slogan{font-family:"Michroma",sans-serif;color:var(--brand-blue-dark);letter-spacing:.5px;white-space:nowrap;
    -webkit-text-stroke:.8px var(--brand-blue-dark);
    text-shadow:0 0 6px var(--white),0 0 3px var(--white)}
  .go{position:absolute;display:flex;align-items:center;justify-content:center;gap:6%;text-decoration:none;
    background:linear-gradient(180deg,var(--gold-top),var(--gold-bottom));border:2px solid #d98c00;border-radius:999px;
    font-family:"Roboto",sans-serif;font-weight:700;color:var(--ink);box-shadow:0 2px 3px rgba(0,0,0,.3)}
  .go svg{height:52%;width:auto}

  /* square banners */
  .banner--square .crest{position:absolute;left:0;top:0;width:100%;height:27%}
  .banner--square .brand-name{position:absolute;left:0;right:0;top:4%;text-align:center;
    font-size:calc(var(--k)*38px);line-height:1.3}
  .banner--square .headline{position:absolute;left:0;right:0;top:28.5%;text-align:center;
    font-size:calc(var(--k)*32px);line-height:1.5;transform:rotate(-1.5deg)}
  .banner--square .service{position:absolute;left:0;right:0;top:46.5%;height:20%;
    display:flex;align-items:center;justify-content:center;font-size:calc(var(--k)*22px);line-height:1.2;padding:0 3%;
    box-shadow:0 2px 0 var(--leaf-green-dark)}
  .banner--square .slogan{position:absolute;left:0;right:0;top:68%;text-align:center;font-size:calc(var(--k)*26px);line-height:1.5}
  .banner--square .go{right:7%;top:83%;width:calc(var(--k)*96px);height:calc(var(--k)*40px);font-size:calc(var(--k)*24px)}

  .b-300x250{left:51px;top:191px;width:451px;height:375px}
  .b-320x250{left:519px;top:191px;width:481px;height:375px}
  .b-336x280{left:51px;top:583px;width:507px;height:422px;--k:1.1}

  /* leaderboard */
  .b-728x90{left:51px;top:41px;width:1098px;height:134px}
  .b-728x90 .crest{position:absolute;left:0;top:0;height:100%;width:300px}
  .b-728x90 .brand-name{position:absolute;left:14px;top:0;height:100%;display:flex;align-items:center;font-size:21px}
  .b-728x90 .headline{position:absolute;left:261px;top:8px;font-size:29px;line-height:1.4}
  .b-728x90 .service{position:absolute;left:247px;top:62px;width:400px;height:57px;text-align:left;
    padding:4px 10px;font-size:19px;line-height:1.3;
    background:linear-gradient(90deg,var(--leaf-green) 75%,rgba(92,184,92,0))}
  .b-728x90 .slogan{position:absolute;left:683px;top:12px;font-size:24px;line-height:1.5}
  .b-728x90 .go{left:977px;top:77px;width:104px;height:47px;font-size:26px}

  .note{position:absolute;left:640px;top:680px;width:432px;text-align:center;
    font-family:"Roboto",sans-serif;font-weight:700;font-size:52px;line-height:1.06;color:var(--caption)}
</style>
</head>
<body>

<section class="banner b-728x90" aria-label="728 by 90 leaderboard">
  <div class="scene" role="img" aria-label="Bright sky with sun rays and a person raising arms in freedom"></div>
  <svg class="crest" viewBox="0 0 300 134" preserveAspectRatio="none" aria-hidden="true">
    <path d="M0 0H262Q238 67 262 134H0Z" fill="var(--leaf-green)"/>
    <path d="M0 0H236Q214 67 236 134H0Z" fill="var(--brand-blue)"/>
  </svg>
  <span class="brand-name">QuietLanternHub</span>
  <p class="headline">Do You value Your privacy?</p>
  <p class="service">Service that deletes Your personal<br>information from the internet.</p>
  <p class="slogan">START BEING FREE</p>
  <a class="go" href="#">GO<svg viewBox="0 0 10 12" aria-hidden="true"><path d="M0 0L10 6L0 12Z" fill="#1b1b1b"/></svg></a>
</section>

<section class="banner banner--square b-300x250" aria-label="300 by 250 banner">
  <div class="scene" role="img" aria-label="Bright sky with sun rays and a person raising arms in freedom"></div>
  <svg class="crest" viewBox="0 0 300 70" preserveAspectRatio="none" aria-hidden="true">
    <path d="M0 0H300V60Q150 44 0 70Z" fill="var(--leaf-green)"/>
    <path d="M0 0H300V52Q150 38 0 62Z" fill="var(--brand-blue)"/>
  </svg>
  <span class="brand-name">QuietLanternHub</span>
  <p class="headline">Do You value Your privacy?</p>
  <p class="service">Service that deletes Your personal<br>information from the internet.</p>
  <p class="slogan">START BEING FREE</p>
  <a class="go" href="#">GO<svg viewBox="0 0 10 12" aria-hidden="true"><path d="M0 0L10 6L0 12Z" fill="#1b1b1b"/></svg></a>
</section>

<section class="banner banner--square b-320x250" aria-label="320 by 250 banner">
  <div class="scene" role="img" aria-label="Bright sky with sun rays and a person raising arms in freedom"></div>
  <svg class="crest" viewBox="0 0 300 70" preserveAspectRatio="none" aria-hidden="true">
    <path d="M0 0H300V60Q150 44 0 70Z" fill="var(--leaf-green)"/>
    <path d="M0 0H300V52Q150 38 0 62Z" fill="var(--brand-blue)"/>
  </svg>
  <span class="brand-name">QuietLanternHub</span>
  <p class="headline">Do You value Your privacy?</p>
  <p class="service">Service that deletes Your personal<br>information from the internet.</p>
  <p class="slogan">START BEING FREE</p>
  <a class="go" href="#">GO<svg viewBox="0 0 10 12" aria-hidden="true"><path d="M0 0L10 6L0 12Z" fill="#1b1b1b"/></svg></a>
</section>

<section class="banner banner--square b-336x280" aria-label="336 by 280 banner">
  <div class="scene" role="img" aria-label="Bright sky with sun rays and a person raising arms in freedom"></div>
  <svg class="crest" viewBox="0 0 300 70" preserveAspectRatio="none" aria-hidden="true">
    <path d="M0 0H300V60Q150 44 0 70Z" fill="var(--leaf-green)"/>
    <path d="M0 0H300V52Q150 38 0 62Z" fill="var(--brand-blue)"/>
  </svg>
  <span class="brand-name">QuietLanternHub</span>
  <p class="headline">Do You value Your privacy?</p>
  <p class="service">Service that deletes Your personal<br>information from the internet.</p>
  <p class="slogan">START BEING FREE</p>
  <a class="go" href="#">GO<svg viewBox="0 0 10 12" aria-hidden="true"><path d="M0 0L10 6L0 12Z" fill="#1b1b1b"/></svg></a>
</section>

<p class="note">See the links in<br>the description<br>to view the<br>animation.</p>

</body>
</html>
```